A wine Label for a new brand of New Zealand Wine

We are looking for a Wine Label for our "Harbor Crest" brand of wines from North Otago New Zealand. We would like the label to perhaps use the HC as a logo and the rest up to the designer. We have our vineyards located in the Waitaki Valley New Zealand which is a southern region with mountains and a river flowing past our vineyard. Photos attached of Dramatic Landscape. Also attached is a basic outline of requirements for the front bottle of the label. The rear bottle label will contain writing about the wines background plus statutory regulations on Alc. Vol, bar code etc. Front Label size to be no Larger than 80mm deep by 100 mm wide. The label can be simple or graphic, whatever the designer chooses.
Target Market(s)
New Wine Brand
Look and feel
Each slider illustrates characteristics of the customer's brand and the style your logo design should communicate.

```html
<!DOCTYPE html>
<html lang="en">
<head>
<meta charset="utf-8">
<title>Harbor Crest Pinot Gris Label</title>
<link rel="stylesheet" href="https://fonts.googleapis.com/css2?family=Old+Standard+TT:wght@400;700&display=swap">
<style>
  :root {
    --backdrop: #aaaaaa;
    --label-black: #1f1f1f;
    --gold: #e4df12;
    --gold-deep: #b8b000;
    --cream: #f4f2ec;
    --sepia-light: #e9e0c8;
    --sepia-mid: #a89a78;
    --sepia-dark: #5a5038;
  }
  * { margin: 0; padding: 0; box-sizing: border-box; }
  html, body {
    width: 970px;
    height: 1200px;
    overflow: hidden;
    background: var(--backdrop);
  }
  .canvas {
    position: relative;
    width: 970px;
    height: 1200px;
  }
  .label {
    position: absolute;
    left: 134px;
    top: 167px;
    width: 702px;
    height: 877px;
    background: var(--label-black);
    font-family: "Old Standard TT", serif;
  }
  .frame {
    position: absolute;
    border: 1.5px solid var(--gold);
  }
  .frame--outer { left: 30px; top: 20px; width: 650px; height: 697px; }
  .frame--inner { left: 22px; top: 31px; width: 648px; height: 696px; }
  .monogram {
    position: absolute;
    left: 284px;
    top: 47px;
    width: 124px;
    height: 124px;
    border: 2px solid var(--gold);
    border-radius: 50%;
    display: flex;
    align-items: center;
    justify-content: center;
    color: var(--gold);
    font-size: 44px;
    font-weight: 700;
  }
  .brand-name {
    position: absolute;
    left: 0;
    width: 100%;
    top: 180px;
    text-align: center;
    color: var(--gold);
    font-size: 80px;
    font-weight: 400;
    line-height: 1;
  }
  .vineyard-view {
    position: absolute;
    left: 130px;
    top: 273px;
    width: 452px;
    height: 300px;
  }
  .varietal {
    position: absolute;
    left: 0;
    width: 100%;
    top: 580px;
    text-align: center;
    color: var(--gold);
    font-size: 62px;
    font-weight: 700;
    line-height: 1;
  }
  .vintage {
    position: absolute;
    left: 0;
    width: 100%;
    top: 660px;
    text-align: center;
    color: var(--gold);
    font-size: 40px;
    font-weight: 700;
    line-height: 1;
  }
  .region {
    position: absolute;
    left: 0;
    width: 100%;
    top: 748px;
    text-align: center;
    color: var(--cream);
    font-size: 26px;
    letter-spacing: 0.5px;
  }
  .origin {
    position: absolute;
    left: 0;
    width: 100%;
    top: 830px;
    text-align: center;
    color: var(--cream);
    font-size: 22px;
    letter-spacing: 2px;
  }
</style>
</head>
<body>
<div class="canvas">
  <section class="label">
    <div class="frame frame--outer"></div>
    <div class="frame frame--inner"></div>

    <div class="monogram">HC</div>
    <h1 class="brand-name">Harbor Crest</h1>

    <svg class="vineyard-view" viewBox="0 0 452 300" role="img"
         aria-label="Sepia photograph of vineyard rows beneath mountains, framed by a gold scrollwork ornament">
      <defs>
        <radialGradient id="scroll-glow" cx="50%" cy="50%" r="50%">
          <stop offset="60%" stop-color="#e4df12" stop-opacity="0.35"/>
          <stop offset="100%" stop-color="#e4df12" stop-opacity="0"/>
        </radialGradient>
        <linearGradient id="landscape-tone" x1="0" y1="0" x2="0" y2="1">
          <stop offset="0%" stop-color="#e9e0c8"/>
          <stop offset="45%" stop-color="#a89a78"/>
          <stop offset="100%" stop-color="#6b6048"/>
        </linearGradient>
      </defs>
      <ellipse cx="226" cy="150" rx="226" ry="150" fill="url(#scroll-glow)"/>
      <ellipse cx="224" cy="152" rx="190" ry="120" fill="url(#landscape-tone)"/>
    </svg>

    <h2 class="varietal">Pinot Gris</h2>
    <p class="vintage">2015</p>

    <p class="region">Waitaki Valley - North Otago</p>
    <p class="origin">New Zealand Wine</p>
  </section>
</div>
</body>
</html>
```